San Francisco corporate relocation liason

I can't seem to find what i have pictured in my head for this project. I am trying to have designed a business card that has either the San Francisco skyline or Golden Gate Bridge Silhouettein gold foil up the around half of the card and below in black letters my personal info that I need to include on card like phone number email etc.

Target Market(s)

Corporate clients I serve

Industry/Entity Type

Business

Contact Information for Business Card

Marla Voskuil
Corporate Relocation Expert
628.309.5182
Transfers.kqd@postvane.com

Requirements
Must have
• I would like the San francisco city skyline or Golden Gate Bridge outline in mettalic gold from the top to the middle of card and below I would like black lettering for contact information. I have included a pic of some inspiration but what I would prefer a more elegant interpretation of the image I included if possible. I had I visioned something with metallic gold and black and white or just black and white...look forward to seeing designs
Nice to have
• If possible something to signify relocation would be a plus but not necessary
• I also included below a few of examples of styles that I am drawn to if they had some element of San Francisco or relocation services

```html
<!DOCTYPE html>
<html lang="en">
<head>
<meta charset="utf-8">
<title>Marla Voskuil — Corporate Relocation Expert</title>
<link rel="stylesheet" href="https://fonts.googleapis.com/css2?family=Lato:wght@400;700&display=swap">
<style>
  :root {
    --backdrop: #8a939c;
    --card: #ffffff;
    --ink: #111111;
    --gold-light: #f6e27a;
    --gold-mid: #d4a92a;
    --gold-deep: #a97c12;
  }
  * { box-sizing: border-box; margin: 0; padding: 0; }
  html, body {
    width: 1200px;
    height: 900px;
    overflow: hidden;
    background: var(--backdrop);
  }
  .stage {
    width: 1200px;
    height: 900px;
    display: flex;
    align-items: center;
    justify-content: center;
  }
  .business-card {
    width: 840px;
    height: 480px;
    background: var(--card);
    box-shadow: 0 18px 40px rgba(0, 0, 0, 0.28);
    display: flex;
    flex-direction: column;
    align-items: center;
    padding-top: 46px;
    font-family: "Lato", sans-serif;
    color: var(--ink);
    text-transform: uppercase;
  }
  .bridge-illustration {
    width: 330px;
    height: 210px;
    display: block;
  }
  .contact-block {
    margin-top: 26px;
    text-align: center;
  }
  .person-name {
    font-weight: 700;
    font-size: 34px;
    letter-spacing: 0.5px;
    line-height: 1.1;
  }
  .person-title {
    font-weight: 400;
    font-size: 17px;
    letter-spacing: 0.3px;
    margin-top: 4px;
  }
  .contact-line {
    font-weight: 400;
    font-size: 21px;
    letter-spacing: 0.4px;
    line-height: 1.3;
  }
  .contact-line.phone { margin-top: 20px; }
</style>
</head>
<body>
  <main class="stage">
    <article class="business-card">
      <svg class="bridge-illustration" viewBox="0 0 330 210" role="img" aria-label="Gold foil illustration of the Golden Gate Bridge with sailboats and gulls over the bay">
        <defs>
          <linearGradient id="gold-foil" x1="0" y1="0" x2="1" y2="1">
            <stop offset="0" stop-color="var(--gold-deep)"/>
            <stop offset="0.45" stop-color="var(--gold-light)"/>
            <stop offset="1" stop-color="var(--gold-mid)"/>
          </linearGradient>
        </defs>
        <rect x="0" y="0" width="330" height="210" rx="4" fill="url(#gold-foil)" opacity="0.85"/>
      </svg>
      <div class="contact-block">
        <h1 class="person-name">Marla Voskuil</h1>
        <p class="person-title">Corporate Relocation Expert</p>
        <p class="contact-line phone">628.309.5182</p>
        <p class="contact-line email">Transfers.kqd@postvane.com</p>
      </div>
    </article>
  </main>
</body>
</html>
```